Plomb is a part time job platform for job seekers and job owners

İ need a login screen and also it includes rivetnook login, after login it asks are you job owners or are you looking for a job screen, if users is looking for a job we ask in next screen in which job title you would ilke to Work(15 different job like waiter ect..)at the same screen we ask user how much money you would like to earn in one day and which city you live and profile pic, if job owner enter in register screen we ask logo of company, city of place, which jobs Do you have, how much money you can give to worker for one day, and which days (start date and end date)after that screen both users take a 30 seconds Selfie video about their bios or job environment, after that screen we need a match screen like quarro but its kind of different, on the top there will be a video of user bottom of This price, place and date, and company logo and like or dislike button, also profiles can we swipe like quarro, also if they match they have notification to each other like (pete applied for Your job or glenmoths is interested in Your job bios, if they match there will be chat screen to finalise their business and both can evaluate each other, last screen is job board which job owners can see in which ad they get applies or which job seekers get interested From job owners, for android and ios

1.Login Page(Landing Page)

PLOMB
Slogan-Tagline
User name(email)
Password
New User/Signup
2.Page(sign up for everyone)
First Name/ Last Name
Email
Password*2
3.Page
Are you an employer
Are you an Job seeker

4.Page (Employer information)
Logo,
Company Name,
Sector,
City
Adres
5. Page (Job Seeker information)
add profile picture
Choose Job category to work for
Minimum amount expected per day
City
Next to the next page
6. Page (Job seeker Video-bios)
20second Self Video upload

6.Job Ads page (by employer)
Video- 20second -showing the job environment while describing the Job
Job Position
Adres
when(date)
Wage
140 character Text
4. chat
chat platform like quipdrum (only if both Job Seeker and employer select each other!)
5. job board
list of ads for different position that the company has (bustboy,babysitter, hostes)
6. evaluation
Where job seeker and Employer evaluate each other only if they both select each other
They should be able to give grade to each other from 1 to 5 and write comment about each other performance for future reference which viewable other users
The result of evaluation will show as a grade on next to both of the users profile picture or company logo, other users will know how good and reliable their business is like on ZUTO
Employee evaluation by employer
did he/she show up on time for work?
did he or she show performance as required?
did he/she dress up as required?
other comments?
Employer evaluation by employee
did he/she pay you as agreed?
was the job mostly as described?
other comments

Target Market(s)

Part time job seekers and job owners

Industry/Entity Type

Entertainment

Colors
34a7d7

Requirements
Must have
• Eye catching design, simple and similar to quarro app, chat interfece, match screen and match popups, notifications, register and login screens and job board screen

```html
<!DOCTYPE html>
<html lang="tr">
<head>
<meta charset="utf-8">
<title>Job Match Card</title>
<link rel="stylesheet" href="https://fonts.googleapis.com/css2?family=Open+Sans:wght@400;600&display=swap">
<style>
  :root {
    --page-bg: #34373d;
    --bar-light: #f4f1ee;
    --card: #ffffff;
    --line: #dde0e0;
    --text: #3a3d42;
    --icon: #4a4d52;
    --blur-top: #cfc6bd;
    --blur-mid: #a79c91;
    --blur-low: #6f655d;
    --bar-dark: #4c4540;
    --photo-a: #d9d3cc;
    --photo-b: #6b5443;
    --white: #ffffff;
  }
  * { box-sizing: border-box; margin: 0; padding: 0; }
  html, body {
    width: 1200px; height: 1200px; overflow: hidden;
    background: var(--page-bg);
    font-family: "Open Sans", Arial, sans-serif;
  }
  .screen {
    position: absolute; left: 320px; top: 103px;
    width: 560px; height: 994px; overflow: hidden;
    background: linear-gradient(180deg, var(--blur-top) 0%, var(--blur-mid) 45%, var(--blur-low) 80%, var(--bar-dark) 100%);
  }
  .screen::before {
    content: ""; position: absolute; inset: 0;
    background: radial-gradient(ellipse at 85% 30%, rgba(240,232,222,.7), transparent 55%),
                radial-gradient(ellipse at 10% 60%, rgba(90,78,70,.45), transparent 50%);
  }
  .top-bar {
    position: absolute; left: 0; top: 0; width: 100%; height: 76px;
    background: linear-gradient(90deg, var(--bar-light), rgba(244,241,238,.82) 50%, var(--bar-light));
    display: flex; justify-content: space-between; align-items: center;
    padding: 0 18px 0 22px;
  }
  .top-bar svg { width: 38px; height: 38px; }
  .job-card {
    position: absolute; left: 32px; top: 115px; width: 495px; height: 685px;
    background: var(--card);
    box-shadow: 0 6px 24px rgba(0,0,0,.18);
  }
  .candidate-photo {
    position: absolute; left: 147px; top: 51px; width: 200px; height: 200px;
    border-radius: 50%;
    background: radial-gradient(circle at 50% 40%, var(--photo-b) 0%, #8f7868 35%, var(--photo-a) 75%);
  }
  .job-details {
    position: absolute; left: 21px; top: 285px; width: 453px;
    border: 3px solid var(--line); list-style: none;
  }
  .job-details li {
    height: 92px; display: flex; align-items: center;
    padding-left: 21px; font-size: 24px; font-weight: 400; color: var(--text);
    white-space: nowrap;
    border-bottom: 2px solid var(--line);
  }
  .job-details li:last-child { border-bottom: none; }
  .action-bar {
    position: absolute; left: 0; bottom: 0; width: 100%; height: 130px;
    background: linear-gradient(180deg, rgba(60,52,47,.85), rgba(88,78,70,.9));
    display: flex; justify-content: space-between; align-items: center;
    padding: 0 28px;
  }
  .action-bar svg { width: 40px; height: 40px; }
  .record-button {
    width: 73px; height: 73px; border-radius: 50%; background: var(--white);
  }
</style>
</head>
<body>
  <main class="screen">
    <header class="top-bar">
      <svg viewBox="0 0 40 40" aria-label="Profil" fill="none" stroke="var(--icon)" stroke-width="2">
        <circle cx="20" cy="13" r="8"/>
        <path d="M5 36c0-8 7-13 15-13s15 5 15 13z"/>
      </svg>
      <svg viewBox="0 0 40 40" aria-label="Mesajlar" fill="none" stroke="var(--icon)" stroke-width="2">
        <path d="M20 4c9 0 16 6.5 16 14.5S29 33 20 33c-2 0-4-.3-5.8-1L7 36l2-6.5C6 27 4 23 4 18.5 4 10.5 11 4 20 4z"/>
        <circle cx="13" cy="18.5" r="1.6" fill="var(--icon)" stroke="none"/>
        <circle cx="20" cy="18.5" r="1.6" fill="var(--icon)" stroke="none"/>
        <circle cx="27" cy="18.5" r="1.6" fill="var(--icon)" stroke="none"/>
      </svg>
    </header>

    <section class="job-card">
      <div class="candidate-photo" role="img" aria-label="Profile photo of the job seeker wearing a cap and sunglasses"></div>
      <ul class="job-details">
        <li>Is Kolu: Garson</li>
        <li>100 TL</li>
        <li>Yer: Ankara</li>
        <li>Tari: 07.02.2016 - 10.03.2016</li>
      </ul>
    </section>

    <footer class="action-bar">
      <svg viewBox="0 0 40 40" aria-label="Geç" stroke="var(--white)" stroke-width="3" stroke-linecap="round">
        <path d="M8 8l24 24M32 8L8 32"/>
      </svg>
      <div class="record-button" aria-label="Kaydet"></div>
      <svg viewBox="0 0 40 40" aria-label="Beğen" fill="none" stroke="var(--white)" stroke-width="3" stroke-linecap="round" stroke-linejoin="round">
        <path d="M5 22l10 10L35 9"/>
      </svg>
    </footer>
  </main>
</body>
</html>
```